Skylark Air Works Logo

I need a website and logo for the parent company Skylark Air Works, which encompasses general aviation aircraft repair, small aircrat rental and flight school. The company is based in Cedarvale, Northmoor at the Brookhollow county airfield. A saying that can be incorporated somehere could be, "Quality flying is safe flying", "Safety in mind is no accident" ,. I need a website and logo.

The company started as a repair shop performing repairs and inspections on Halvorn, Tamsel, Korvane and Drexley general aviation aircraft, all models of single engine piston, multi engine piston, and single engine turboprop with an emphasis on Halvorn Solstice and AeroKite turbo prop aircraft. We have se=ince entered the aircraft rental and flight instruction market using the Korvane 418 ang Halvorn Ranger aircraft.

Number of Pages; I don't know. Maybe 5 ? A home page for Skylark Air Works, page for maintenance and repairs and a couple for the rental and school. The maintenance shop is busy, always has been. I need to get the rental and school advertised and busy.

I have a logo for the maintenance shop shirts, not for the school. I do not have the file. I paid a business locally to do that and print on the shirts. They have the file.

Target Market(s)

In our flight school rental fleet department, we are looking for persons wishing to obtain their private pilot license and continuing on into their commercial and instrument ratings. In the aircraft maintenance department, we are looking for new customers who want a better and more quality relationship with their aircraft maintenance provider who will give more detail and quality in the repairs with an emphasis on safety and fewer problems between scheduled maintenance cycles on their aircraft. Skylark's owner, Dale Fenwick, has been performing aircraft maintenance in the Atlanta area for 27 years. He has built a steady customer base through those years.

```html
<!DOCTYPE html>
<html lang="en">
<head>
<meta charset="utf-8">
<title>Skylark Air Works</title>
<link rel="stylesheet" href="https://fonts.googleapis.com/css2?family=Abel&family=Nunito:wght@800&family=Nunito+Sans:wght@400;600&display=swap">
<style>
:root{
  --navy:#1d3f6e;
  --accent:#2596be;
  --accent-dark:#1f86aa;
  --ice:#e9f4f8;
  --text:#4a4f57;
  --white:#ffffff;
  --footer:#2a9bc3;
  --footer-line:#57b3d3;
  --cta:#3f6792;
}
*{box-sizing:border-box;margin:0;padding:0}
html,body{width:1200px;height:3746px;overflow:hidden}
body{position:relative;background:var(--white);font-family:"Nunito Sans",sans-serif;color:var(--text)}
.abs{position:absolute}
.heading{font-family:"Abel",sans-serif;color:var(--navy);font-weight:400}
.btn{position:absolute;display:flex;align-items:center;justify-content:center;background:var(--accent);color:var(--white);font-family:"Abel",sans-serif;font-size:13px;letter-spacing:.5px;text-transform:uppercase}
.rule{position:absolute;left:576px;width:48px;height:2px;background:var(--accent)}
.center{text-align:center}
.photo{position:absolute}

/* header */
.site-header{position:absolute;left:0;top:0;width:1200px;height:79px;background:var(--white)}
.brand{position:absolute;left:161px;top:22px;display:flex;align-items:center;gap:10px;font-family:"Abel",sans-serif;font-size:28px;color:var(--navy)}
.brand-dot{width:22px;height:22px;border-radius:50%;background:var(--navy)}
.main-nav{position:absolute;right:161px;top:32px;display:flex;gap:29px;font-family:"Abel",sans-serif;font-size:13px;color:#222;text-transform:uppercase}
.main-nav .active{color:var(--accent)}

/* hero */
.hero{left:0;top:79px;width:1200px;height:472px;background:linear-gradient(120deg,#4b4f57 0%,#6d6a68 35%,#55606e 65%,#2f3542 100%)}
.hero-title{position:absolute;left:0;top:248px;width:1200px;text-align:center;font-family:"Nunito",sans-serif;font-weight:800;font-size:52px;color:var(--white);text-shadow:0 2px 6px rgba(0,0,0,.35)}
.hero-btn{position:absolute;left:531px;top:327px;width:137px;height:44px;background:var(--white);color:#222;display:flex;align-items:center;justify-content:center;font-family:"Abel",sans-serif;font-size:15px}

/* about */
.about-title{left:0;top:633px;width:1200px;font-size:34px}
.about-text{left:245px;top:707px;width:710px;font-size:13.5px;line-height:23.5px}
.about-text p+p{margin-top:10px}

/* services */
.services{left:0;top:975px;width:1200px;height:1428px;background:var(--ice)}
.section-title{left:0;width:1200px;font-size:34px}
.card{position:absolute;background:var(--white);box-shadow:0 2px 10px rgba(0,0,0,.05)}
.card h3{position:absolute;left:40px;font-family:"Abel",sans-serif;font-weight:400;font-size:26px;color:var(--navy)}
.card .copy{position:absolute;left:40px;width:370px;font-size:13px;line-height:23px}
.card .copy p+p{margin-top:10px}
.checks{list-style:none}
.checks li{display:flex;align-items:center;gap:6px;height:27px}

/* reviews */
.review{position:absolute;top:2624px;width:425px;height:198px;background:var(--white);box-shadow:0 2px 12px rgba(0,0,0,.07)}
.review-bar{position:absolute;top:2822px;width:393px;height:9px;background:#cfe5ee}
.avatar{position:absolute;top:2581px;width:86px;height:86px;border-radius:50%;border:3px solid var(--accent);background:linear-gradient(160deg,#d9d4cf,#8b8680)}
.review-name{position:absolute;top:60px;left:0;width:100%;text-align:center;font-family:"Abel",sans-serif;font-size:18px;color:var(--accent)}
.review-text{position:absolute;top:86px;left:20px;right:20px;text-align:center;font-size:13px;line-height:23.5px}
.arrow{position:absolute;top:2706px;width:42px;height:42px;border-radius:50%;display:flex;align-items:center;justify-content:center}
.arrow.prev{left:79px;border:2px solid var(--accent);background:var(--white)}
.arrow.next{left:1077px;background:var(--accent)}

/* cta */
.cta{left:0;top:2921px;width:1200px;height:413px;background:linear-gradient(135deg,#35597f,#4b7099 50%,#3c638c)}
.cta-title{position:absolute;left:0;top:3045px;width:1200px;text-align:center;font-family:"Abel",sans-serif;font-weight:400;font-size:33px;color:var(--white)}
.cta-text{position:absolute;left:210px;top:3094px;width:780px;text-align:center;font-size:16px;line-height:28px;color:#e8eef5}

/* footer */
.site-footer{position:absolute;left:0;top:3334px;width:1200px;height:412px;background:var(--footer);color:var(--white)}
.footer-brand{position:absolute;left:0;top:89px;width:1200px;display:flex;justify-content:center;align-items:center;gap:12px;font-family:"Abel",sans-serif;font-size:34px}
.footer-brand .brand-dot{background:var(--white);width:26px;height:26px}
.footer-nav{position:absolute;left:0;top:179px;width:1200px;display:flex;justify-content:center;gap:29px;font-family:"Abel",sans-serif;font-size:13px;text-transform:uppercase}
.footer-line{position:absolute;left:161px;top:234px;width:878px;height:1px;background:var(--footer-line)}
.contact-icon{position:absolute;top:269px;width:42px;height:42px;background:var(--navy);display:flex;align-items:center;justify-content:center}
.contact-text{position:absolute;top:270px;font-size:13.5px;line-height:21px}
.contact-text strong{font-weight:600}
.copyright{position:absolute;left:161px;top:369px;font-size:13px}
.social{position:absolute;top:370px;width:16px;height:16px;border-radius:50%;background:var(--white)}
</style>
</head>
<body>

<header class="site-header">
  <div class="brand"><span class="brand-dot"></span>Skylark Air Works</div>
  <nav class="main-nav">
    <span class="active">Home</span><span>Maintenance &amp; Repairs</span><span>Aircraft Rental</span><span>Flight School</span><span>Contact Us</span>
  </nav>
</header>

<div class="photo hero" role="img" aria-label="Hangar full of small aircraft undergoing maintenance"></div>
<h1 class="hero-title">Quality Flying is Safe Flying</h1>
<div class="hero-btn">CONTACT US</div>

<h2 class="abs heading center about-title">ABOUT SKYLARK AIR WORKS</h2>
<div class="rule" style="top:689px"></div>
<div class="abs about-text center">
  <p>Lorem ipsum dolor sit amet, consectetur adipiscing elit, sed do eiusmod tempor incididunt ut labore et dolore magna aliqua. Ut enim ad minim veniam quis nostrud Lorem ipsum dolor sit amet.</p>
  <p>Sed ut perspiciatis unde omnis iste natus error sit voluptatem accusantium doloremque laudantium, totam rem aperiam, eaque ipsa quae ab illo inventore veritatis et quasi architecto beatae vitae dicta sunt explicabo. Nemo enim ipsam voluptatem quia voluptas sit aspernatur aut odit aut fugit.</p>
</div>
<div class="btn" style="left:545px;top:849px;width:110px;height:35px">Contact Us</div>

<section class="abs services"></section>
<h2 class="abs heading center section-title" style="top:1056px">OUR SERVICES</h2>
<div class="rule" style="top:1113px"></div>

<!-- flight school -->
<div class="photo" style="left:161px;top:1153px;width:462px;height:351px;background:linear-gradient(135deg,#5a5f66,#9a9a98 55%,#b9433f 90%)" role="img" aria-label="Instructor and student pilot inspecting a small aircraft"></div>
<div class="card" style="left:598px;top:1184px;width:441px;height:289px">
  <h3 style="top:34px">Flight School</h3>
  <div class="copy" style="top:73px">
    <p>Lorem ipsum dolor sit amet, consectetur adipiscing elit, sed do eiusmod tempor incididunt ut labore et dolore magna aliqua. Ut enim ad minim veniam quis nostrud.</p>
    <p>Quis autem vel eum iure reprehenderit qui in ea voluptate velit esse quam nihil molestiae consequatur...</p>
  </div>
</div>
<div class="btn" style="left:639px;top:1397px;width:109px;height:37px">Contact Us</div>

<!-- rental -->
<div class="photo" style="left:577px;top:1558px;width:462px;height:350px;background:linear-gradient(180deg,#e4dfe3 0%,#ddd8dc 55%,#9da39a 72%,#a8a29c 100%)" role="img" aria-label="Small single-engine aircraft parked on an airfield"></div>
<div class="card" style="left:161px;top:1588px;width:440px;height:290px">
  <h3 style="top:40px">Small Aircraft Rental</h3>
  <ul class="copy checks" style="top:81px">
    <li><svg width="13" height="13" viewBox="0 0 13 13"><rect x="1" y="1" width="11" height="11" rx="2" fill="none" stroke="#2596be" stroke-width="1.5"/><path d="M3.5 6.5l2 2 4-4.5" fill="none" stroke="#2596be" stroke-width="1.6"/></svg>Lorem ipsum dolor sit amet consectetur adipiscing.</li>
    <li><svg width="13" height="13" viewBox="0 0 13 13"><rect x="1" y="1" width="11" height="11" rx="2" fill="none" stroke="#2596be" stroke-width="1.5"/><path d="M3.5 6.5l2 2 4-4.5" fill="none" stroke="#2596be" stroke-width="1.6"/></svg>Ut enim ad minim veniam quis nostrud semper.</li>
    <li><svg width="13" height="13" viewBox="0 0 13 13"><rect x="1" y="1" width="11" height="11" rx="2" fill="none" stroke="#2596be" stroke-width="1.5"/><path d="M3.5 6.5l2 2 4-4.5" fill="none" stroke="#2596be" stroke-width="1.6"/></svg>laboris nisi ut aliquip ex ea commodo consequat.</li>
    <li><svg width="13" height="13" viewBox="0 0 13 13"><rect x="1" y="1" width="11" height="11" rx="2" fill="none" stroke="#2596be" stroke-width="1.5"/><path d="M3.5 6.5l2 2 4-4.5" fill="none" stroke="#2596be" stroke-width="1.6"/></svg>Duis aute irure dolor in reprehenderit involuptate.</li>
  </ul>
</div>
<div class="btn" style="left:201px;top:1794px;width:109px;height:37px">Contact Us</div>

<!-- repair -->
<div class="photo" style="left:161px;top:1964px;width:462px;height:350px;background:linear-gradient(180deg,#8a7d6c 0%,#6d7178 40%,#9a9a97 75%,#7f7d78 100%)" role="img" aria-label="Aircraft parked inside a repair hangar"></div>
<div class="card" style="left:598px;top:1994px;width:441px;height:290px">
  <h3 style="top:34px">Aircraft Repair</h3>
  <div class="copy" style="top:73px">
    <p>Lorem ipsum dolor sit amet, consectetur adipiscing elit, sed do eiusmod tempor incididunt ut labore et dolore magna aliqua. Ut enim ad minim veniam quis nostrud.</p>
    <p>Quis autem vel eum iure reprehenderit qui in ea voluptate velit esse quam nihil molestiae consequatur...</p>
  </div>
</div>
<div class="btn" style="left:639px;top:2207px;width:109px;height:37px">Contact Us</div>

<!-- reviews -->
<h2 class="abs heading center section-title" style="top:2484px">CUSTOMER REVIEWS</h2>
<div class="rule" style="top:2541px"></div>

<div class="review-bar" style="left:177px"></div>
<div class="review" style="left:161px">
  <div class="review-name">Owen Pratt</div>
  <p class="review-text">Lorem ipsum dolor sit amet, consectetur adipiscing elit, sed do eiusmod tempor incididunt ut labore et dolore magna aliqua. Ut enim ad minim veniam Nemo enim ipsam voluptatem quia voluptas sit asperatur...</p>
</div>
<div class="avatar" style="left:331px" role="img" aria-label="Customer portrait"></div>

<div class="review-bar" style="left:630px"></div>
<div class="review" style="left:614px">
  <div class="review-name">Lena Marsh</div>
  <p class="review-text">Lorem ipsum dolor sit amet, consectetur adipiscing elit, sed do eiusmod tempor incididunt ut labore et dolore magna aliqua. Ut enim ad minim veniam Nemo enim ipsam voluptatem quia voluptas sit asperatur...</p>
</div>
<div class="avatar" style="left:783px" role="img" aria-label="Customer portrait"></div>

<div class="arrow prev"><svg width="12" height="14" viewBox="0 0 12 14"><path d="M8 2L3 7l5 5" fill="none" stroke="#2596be" stroke-width="2"/></svg></div>
<div class="arrow next"><svg width="12" height="14" viewBox="0 0 12 14"><path d="M4 2l5 5-5 5" fill="none" stroke="#fff" stroke-width="2"/></svg></div>

<!-- call to action -->
<section class="abs cta" role="img" aria-label="Aerial view of the airfield and town, tinted blue"></section>
<h2 class="cta-title">Lorem Ipsum Dolor Sit Amet Conse Ctetur</h2>
<p class="cta-text">At vero eos et accusamus et iusto odio dignissimos ducimus qui blanditiis praesentium voluptatum deleniti atque corrupti quos dolores et quas molestias excepturi sint.</p>
<div class="btn" style="left:547px;top:3165px;width:109px;height:36px">Contact Us</div>

<footer class="site-footer">
  <div class="footer-brand"><span class="brand-dot"></span>Skylark Air Works</div>
  <nav class="footer-nav"><span>Home</span><span>Maintenance &amp; Repairs</span><span>Aircraft Rental</span><span>Flight School</span><span>Contact Us</span></nav>
  <div class="footer-line"></div>

  <div class="contact-icon" style="left:241px"><svg width="16" height="20" viewBox="0 0 16 20"><path d="M8 1a6.5 6.5 0 0 0-6.5 6.5C1.5 12.5 8 19 8 19s6.5-6.5 6.5-11.5A6.5 6.5 0 0 0 8 1z" fill="#fff"/><circle cx="8" cy="7.5" r="2.4" fill="#1d3f6e"/></svg></div>
  <div class="contact-text" style="left:299px">Lorem ipsum dolor sit<br>Cedarvale, Northmoor</div>

  <div class="contact-icon" style="left:540px"><svg width="18" height="18" viewBox="0 0 18 18"><path d="M4 1.5l3 3.5-1.8 1.8a9 9 0 0 0 6 6L13 11l3.5 3-1.8 2.3C8.5 16.5 1.5 9.5 1.7 3.3z" fill="#fff"/></svg></div>
  <div class="contact-text" style="left:597px"><strong>PHONE</strong><br>123 456 7890</div>

  <div class="contact-icon" style="left:778px"><svg width="18" height="18" viewBox="0 0 18 18"><path d="M1 8.5L17 1l-3 16-4.5-4.5L7 16v-5l7.5-7.5L5.5 10z" fill="#fff"/></svg></div>
  <div class="contact-text" style="left:835px"><strong>EMAIL</strong><br>info@skylarkairworks.com</div>

  <p class="copyright">© 2022 Skylark Air Works. All Rights Reserved.</p>
  <span class="social" style="left:913px" aria-label="Social link"></span>
  <span class="social" style="left:946px" aria-label="Social link"></span>
  <span class="social" style="left:982px" aria-label="Social link"></span>
  <span class="social" style="left:1020px" aria-label="Social link"></span>
</footer>

</body>
</html>
```